PowerPoint Template Needed for Investment Firm

Meridale Capital Management is an emerging wealth management firm based in New Jersey. It offers superior investment returns to high net worth individuals and institutions by finding undervalued assets.

We recently selected a company logo which was inspired by the Meridale constellation. Beta Tucanae is a group of six stars, containing star cluster 47 Tucanae, rated the second brightest object in the sky.

Now we need a PowerPoint template with the designs for the following:

1. Title/cover page slide
2. Content slide with title
3. Section slide - to introduce a new section
4. Final slide - with contact information

The slides will be used at investor presentations, that is, to provide information about the company to potential investors. Since we are an investment firm, the design should project a sense of stability, growth and professionalism. The owner is interested in something simple yet striking, which of course is consistent with the logo. I'm thinking more conservative colors and Sans Serif fonts.

I plan on changing the status to non-refundable once I see some designs that I really like.

Target Market(s)

Wealthy individuals, probably middle aged or older, in the US

Industry/Entity Type

Conservative

Requirements
Must have
• Sans serif fonts
Clean, very professional look
Conservative colors that complement existing logo
Should not have
• Anything too busy or complicated

```html
<!DOCTYPE html>
<html lang="en">
<head>
<meta charset="utf-8">
<title>Financial Returns – Meridale Capital Management</title>
<link rel="stylesheet" href="https://fonts.googleapis.com/css2?family=Open+Sans:wght@400;600;700&display=swap">
<style>
  :root {
    --navy: #0a2a8f;
    --navy-deep: #071f6e;
    --title-blue: #0d2fa3;
    --slice-blue: #0a66e2;
    --slice-blue-side: #062b5f;
    --slice-orange: #f3950f;
    --slice-orange-side: #cf7800;
    --brand-text: #2b3a4a;
    --rule-grey: #cfd3d8;
    --white: #ffffff;
  }
  * { margin: 0; padding: 0; box-sizing: border-box; }
  html, body { width: 1200px; height: 900px; overflow: hidden; }
  body { font-family: "Open Sans", Arial, sans-serif; background: var(--white); }

  .slide { position: relative; width: 1200px; height: 900px; overflow: hidden; background: var(--white); }

  .backdrop { position: absolute; inset: 0; }

  .header-band {
    position: absolute; left: 0; top: 0; width: 1200px; height: 132px;
    background: linear-gradient(180deg, #0c2f9a 0%, var(--navy-deep) 100%);
  }
  .header-rule {
    position: absolute; left: 0; top: 132px; width: 1200px; height: 12px;
    background: linear-gradient(180deg, #c9ccd1 0%, rgba(255,255,255,0) 100%);
  }
  .slide-title {
    position: absolute; left: 45px; top: 38px;
    color: var(--white); font-weight: 700; font-size: 39px; letter-spacing: 0.5px;
  }

  .brand-badge { position: absolute; left: 900px; top: 0; width: 290px; height: 240px; }
  .brand-mark {
    position: absolute; left: 1000px; top: 14px; width: 92px; height: 92px;
    border-radius: 12px; background: linear-gradient(160deg, #1b3fa8 0%, #0a1f66 100%);
  }
  .brand-name {
    position: absolute; left: 912px; top: 112px; width: 264px; text-align: center;
    color: var(--brand-text); font-weight: 600; line-height: 1.1;
  }
  .brand-name .primary { display: block; font-size: 31px; letter-spacing: 2px; }
  .brand-name .secondary { display: block; font-size: 17px; margin-top: 4px; }

  .section-heading {
    position: absolute; left: 42px; top: 178px;
    color: var(--title-blue); font-weight: 700; font-size: 25px;
  }

  .returns-chart { position: absolute; left: 0; top: 0; width: 1200px; height: 900px; }
  .chart-label { font-family: "Open Sans", Arial, sans-serif; font-weight: 700; font-size: 27px; fill: var(--white); }

  .footer-band {
    position: absolute; left: 0; top: 849px; width: 1200px; height: 51px;
    background: linear-gradient(180deg, #0c2f9a 0%, var(--navy-deep) 100%);
  }
  .footer-url {
    position: absolute; left: 36px; top: 856px;
    color: var(--white); font-weight: 600; font-size: 25px;
  }
  .page-number {
    position: absolute; left: 1128px; top: 837px; width: 51px; height: 54px;
    background: var(--white); border: 2px solid var(--navy); border-radius: 8px;
    color: var(--navy); font-weight: 700; font-size: 25px;
    display: flex; align-items: center; justify-content: center;
  }
</style>
</head>
<body>
<main class="slide">
  <svg class="backdrop" width="1200" height="900" viewBox="0 0 1200 900" aria-hidden="true">
    <defs>
      <linearGradient id="swoosh" x1="0" y1="0" x2="1" y2="1">
        <stop offset="0" stop-color="#e9ebee" stop-opacity="0.9"/>
        <stop offset="1" stop-color="#ffffff" stop-opacity="0"/>
      </linearGradient>
    </defs>
    <path d="M0 140 C 300 260, 700 200, 1200 380 L1200 140 Z" fill="url(#swoosh)"/>
    <path d="M520 140 C 780 260, 980 420, 1200 820 L1200 140 Z" fill="url(#swoosh)" opacity="0.7"/>
    <path d="M0 300 C 250 220, 500 200, 760 140 L0 140 Z" fill="#f1f2f4" opacity="0.8"/>
  </svg>

  <div class="header-band"></div>
  <div class="header-rule"></div>
  <h1 class="slide-title">FINANCIAL RETURNS</h1>

  <svg class="brand-badge" viewBox="900 0 290 240" aria-hidden="true">
    <polygon points="912,0 1176,0 1176,172 1046,228 912,172" fill="#ffffff" stroke="#c5c9ce" stroke-width="2"/>
  </svg>
  <div class="brand-mark"></div>
  <div class="brand-name">
    <span class="primary">MERIDALE</span>
    <span class="secondary">Capital Management</span>
  </div>

  <h2 class="section-heading">FINANCIAL RETURNS CONTENT</h2>

  <svg class="returns-chart" viewBox="0 0 1200 900" role="img" aria-label="Pie chart of financial returns split into two parts">
    <path d="M346 504 A220 110 0 0 0 648 606 L648 699 A220 110 0 0 1 346 597 Z" fill="var(--slice-orange-side)"/>
    <path d="M648 606 A220 110 0 0 0 786 504 L786 597 A220 110 0 0 1 648 699 Z" fill="var(--slice-blue-side)"/>
    <path d="M566 504 L648 606 A220 110 0 1 0 346 504 Z" fill="var(--slice-blue)"/>
    <path d="M566 504 L346 504 A220 110 0 0 0 648 606 Z" fill="var(--slice-orange)"/>
    <text class="chart-label" x="472" y="466">CONTENT HERE</text>
    <text class="chart-label" x="428" y="541">CONTENT</text>
    <text class="chart-label" x="428" y="578">HERE</text>
  </svg>

  <footer>
    <div class="footer-band"></div>
    <div class="footer-url">www.meridalecapmgmt.com</div>
    <div class="page-number">01</div>
  </footer>
</main>
</body>
</html>
```